Wordpress Template für Weinkommunikation
Zielgruppe
Kunden und potentielle Kunden, die sich über meine Dienstleistungen und mich informieren wollen.
Meine Arbeitsschwerpunkte sind Kommunikation, PR und Events im Weinbereich.
Meine persönlichen Wein-Schwerpunktländer sind Spanien und Portugal. Die Kunden sind von dort, meine Arbeit ist in Deutschland.
Aufgabenstellung
Ich möchte meine bestehende Website endlich mal richtig gestalten lassen.
- Startseite soll statisch sein.
- Weitere Seiten sollen auch statisch möglich sein.
- 2- oder 3-spaltig
- Template muss Widget-fähig sein
- Möglichkeit der Zweisprachigkeit

```html
<!DOCTYPE html>
<html lang="de">
<head>
<meta charset="utf-8">
<title>Rebe &amp; Rat – Weinkommunikation &amp; mehr</title>
<link href="https://fonts.googleapis.com/css2?family=Arimo:wght@400;700&family=Rosario:wght@300;400&family=Nothing+You+Could+Do&display=swap" rel="stylesheet">
<style>
:root{
  --page:#fcf3e8;
  --wine:#8e1a22;
  --wine-dark:#6e1018;
  --wine-light:#b0333a;
  --paper:#ffffff;
  --ink:#222222;
  --muted:#666666;
  --script:#2a4fb0;
}
*{box-sizing:border-box;margin:0;padding:0}
html,body{width:975px;height:1200px;overflow:hidden}
body{background:var(--page);font-family:"Arimo",Arial,sans-serif;color:var(--ink);position:relative}
.abs{position:absolute}

.brand{left:168px;top:0;width:238px;height:62px;background:var(--paper);box-shadow:0 2px 5px rgba(0,0,0,.25);display:flex;align-items:center;justify-content:center;gap:10px}
.brand-dot{width:18px;height:18px;border-radius:50%;background:var(--wine)}
.brand-name{font-family:"Rosario",sans-serif;font-size:20px;color:var(--wine-dark)}

.site{left:128px;top:79px;width:721px;height:262px;background:var(--paper);box-shadow:0 1px 5px rgba(0,0,0,.2)}
.nav{height:40px;display:flex;align-items:center;padding-left:18px;border-bottom:3px solid var(--wine)}
.nav a{font-size:11px;color:var(--muted);text-decoration:none;padding:5px 10.5px;white-space:nowrap}
.nav a.active{background:var(--wine);color:#fff;font-weight:700;padding:6px 11px;margin-right:2px}
.hero{position:absolute;left:0;top:40px;width:721px;height:222px}
.hero-photo{position:absolute;left:0;top:0;width:337px;height:222px;background:radial-gradient(circle at 35% 55%,#3a0a10 0 22%,#b49a6a 23%,#e9d39c 45%,#6d5538 80%,#2c2012)}
.dots{position:absolute;left:14px;bottom:8px;display:flex;gap:6px}
.dots span{width:7px;height:7px;border-radius:50%;background:#fff;opacity:.85}
.hero-panel{position:absolute;left:337px;top:0;width:384px;height:222px;background:linear-gradient(90deg,var(--wine-dark),var(--wine-light));color:#fff;text-align:center}
.hero-title{font-family:"Rosario",sans-serif;font-size:27px;margin-top:20px}
.hero-quote{font-family:"Nothing You Could Do",cursive;font-size:22px;line-height:31px;margin-top:12px}
.hero-src{font-size:10px;font-weight:700;text-align:right;padding-right:58px}
.hero-trans{font-family:"Nothing You Could Do",cursive;font-size:13px;position:absolute;bottom:12px;right:10px}
.feed{left:849px;top:244px;width:38px;height:36px;background:linear-gradient(#f7a54a,#e8741b);border-radius:4px}
.follow{left:849px;top:291px;width:55px;height:32px;background:linear-gradient(#e6f3fb,#a9d2ee);border-radius:3px;border:1px solid #8ab}

.content{left:128px;top:356px;width:533px;height:666px;background:var(--paper);border-top:3px solid var(--wine);box-shadow:0 1px 5px rgba(0,0,0,.2)}
.content h1{font-family:"Rosario",sans-serif;font-weight:300;font-size:29px;color:var(--wine);position:absolute;left:21px;top:22px}
.motto{position:absolute;left:24px;top:88px;width:340px;font-family:"Nothing You Could Do",cursive;font-size:14px;line-height:16.5px;color:var(--script)}
.motto p{margin-bottom:16px}
.signature{position:absolute;left:188px;top:285px;font-family:"Nothing You Could Do",cursive;font-size:18px;color:var(--script)}
.portrait-frame{position:absolute;left:381px;top:72px;width:131px;height:188px;background:#f5ecd8;padding:6px;transform:rotate(1deg);box-shadow:1px 2px 5px rgba(0,0,0,.35)}
.portrait{width:100%;height:100%;background:linear-gradient(160deg,#6b5a48,#2a2a30 55%,#3a4a58)}
.text{position:absolute;left:26px;top:322px;width:485px;font-size:10.4px;line-height:13.6px}
.text p{margin-bottom:13.6px}
.dropcap{float:left;font-family:"Rosario",sans-serif;font-size:40px;line-height:32px;color:var(--wine);margin-right:2px}

.widget{left:675px;width:174px;background:var(--paper);box-shadow:0 1px 5px rgba(0,0,0,.2)}
.widget h2{height:49px;background:linear-gradient(var(--wine-light),var(--wine-dark));color:#fff;font-family:"Rosario",sans-serif;font-weight:400;font-size:22px;padding:10px 0 0 16px}
.field{display:flex;align-items:center;justify-content:space-between;padding:6px 6px 0 21px;font-size:9.5px;color:#999}
.btn{width:37px;height:17px;border:1px solid #999;border-radius:2px;background:linear-gradient(#fff,#ddd);font-size:9.5px;color:#333;text-align:center;line-height:15px}
.book-title{font-size:11px;font-weight:700;color:var(--wine);padding:19px 0 0 20px}
.book{width:63px;height:82px;margin:8px 0 0 51px;background:linear-gradient(#b0272c,#7d1218);box-shadow:1px 1px 3px rgba(0,0,0,.4)}
.widget .blurb{font-size:10px;line-height:13px;padding:10px 10px 0 20px}
.blurb a{color:var(--wine)}
.wine-blurb{position:absolute;left:16px;top:78px;width:90px;font-size:9.6px;line-height:12.4px}
.wine-blurb a{color:var(--wine)}
.bottle{position:absolute;left:114px;top:66px;width:40px;height:155px;background:linear-gradient(90deg,#6f7a3a,#c8cf8a 45%,#5d6a2a);border-radius:14px 14px 4px 4px}

.footer{left:128px;top:1037px;width:721px;height:75px;background:linear-gradient(var(--wine-light),var(--wine-dark));color:#fff;box-shadow:0 1px 5px rgba(0,0,0,.3)}
.copy{position:absolute;left:29px;top:9px;font-size:10px}
.fcol{position:absolute;top:9px;width:64px;text-align:center;font-size:9px;line-height:11px}
.fcol b{font-size:10px}
.fcol span{color:#f1c9c9}
.flinks{position:absolute;right:21px;top:9px;font-size:10px;display:flex;gap:17px}
.note{position:absolute;left:30px;top:40px;width:670px;font-size:5.8px;line-height:12px}
</style>
</head>
<body>
<header class="brand abs"><span class="brand-dot"></span><span class="brand-name">Rebe &amp; Rat</span></header>

<div class="site abs">
  <nav class="nav">
    <a class="active">Willkommen</a><a>About</a><a>Referenzen</a><a>Buchtipps</a><a>Wein-News</a><a>Wein-Glossar</a><a>Links</a><a>Photovoltaik</a><a>Kontakt</a><a>My Blog</a>
  </nav>
  <section class="hero">
    <div class="hero-photo" role="img" aria-label="Rotweinglas vor warm verschwommenem Hintergrund">
      <div class="dots"><span></span><span></span><span></span><span></span><span></span></div>
    </div>
    <div class="hero-panel">
      <div class="hero-title">Weinkommunikation &amp; mehr</div>
      <div class="hero-quote">"Salud, dinero y amor ...<br>... y el tiempo para disfrutarlo!"</div>
      <div class="hero-src">Spanischer Trinkspruch</div>
      <div class="hero-trans">"Gesundheit, Geld und Liebe und die Zeit es zu genießen!"</div>
    </div>
  </section>
</div>
<div class="feed abs" aria-label="Feed"></div>
<div class="follow abs" aria-label="Folgen"></div>

<main class="content abs">
  <h1>Herzlich Willkommen bei Rebe &amp; Rat</h1>
  <div class="motto">
    <p>Life is good!</p>
    <p>Ich habe nur dieses eine Leben, daher nehme ich<br>es so, wie es ist. Und sehe es positiv!<br>Warum sollte ich es mir selber schwer machen und<br>schwarz sehen?<br>Positiv denkend, positiv gestimmt, geht vieles<br>leichter und letztendlich erfolgreicher.</p>
    <p>Do what you like.<br>Like what you do.</p>
  </div>
  <div class="signature">Lars K. Brenner</div>
  <div class="portrait-frame"><div class="portrait" role="img" aria-label="Porträtfoto des Inhabers mit Schal"></div></div>
  <div class="text">
    <p><span class="dropcap">M</span>it Rebe &amp; Rat möchte ich Ihnen vor allem mein Wissen über Wein - insbesondere der Iberischen Halbinsel - über die Weinbau-Länder, die unterschiedlichen Regionen, die abwechslungsreichen Landschaften, die unzähligen Kellereien, die Winzerpersönlichkeiten, aber auch meine ganz persönlichen Eindrücke und Erlebnisse zur Kultur, zur Gastronomie, zu den Menschen und zum Leben in Spanien, Portugal, der Weinwelt und zum Thema Genuss allgemein zugänglich machen.</p>
    <p>Durch die langjährige Erfahrung im internationalen Weingrosshandel und der Weinszene sind die Bereiche Kommunikation, PR und Marketing, sowie die Sortiments- und Einkaufsberatung, neben den Schulungen ein wichtiger Bestandteil des Angebotes.<br>Speziell im institutionellen Bereich biete ich Verbänden, Regionen und Ländern die Möglichkeit, sich über den deutschen Weinmarkt kundig zu machen, zu eruieren wo und wie sie ihre Produkte am sinnvollsten anbieten können. Hierzu gehört auch die Kommunikations- und Pressearbeit, sowie die Konzeption, Planung und Durchführung von Veranstaltungen.</p>
    <p>In Partnerschaft mit einer Vielzahl von Sommeliers, Weinprofis und anderen Freiberuflern können wir Ihnen darüber hinaus ein breites Spektrum an Leistungen rund um das Thema Wein und Genuss anbieten. Das garantiert Ihnen massgeschneiderte Weinkompetenz ganz nach Ihrem Geschmack und Ihren Wünschen!</p>
    <p>Sprechen Sie uns einfach an. Wir sind für Sie da!</p>
  </div>
</main>

<aside>
  <section class="widget abs" style="top:356px;height:82px">
    <h2>Suche</h2>
    <div class="field">Suche...<span class="btn">Go</span></div>
  </section>
  <section class="widget abs" style="top:450px;height:231px">
    <h2>Neuer Buchtipp</h2>
    <div class="book-title">Rebenhaus Deutschland</div>
    <div class="book" role="img" aria-label="Buchcover in Rot"></div>
    <div class="blurb">Ut enim ad minim veniam, quis nostrud exercitation ullamco laboris nisi ut aliquip <a>mehr...</a></div>
  </section>
  <section class="widget abs" style="top:697px;height:90px">
    <h2>Newsletter</h2>
    <div class="field">Bitte eMail eingeben...<span class="btn">Go</span></div>
  </section>
  <section class="widget abs" style="top:791px;height:234px">
    <h2>Best of: Wein</h2>
    <div class="wine-blurb">Domaine Vallière Sauvignon Prestige 2009 Touraine Lorem ipsum dolor amet, consectetur adipisicing elit, sed do eiusmod tempor incididunt ut labore<br><br><a>Details...</a></div>
    <div class="bottle" role="img" aria-label="Weißweinflasche"></div>
  </section>
</aside>

<footer class="footer abs">
  <div class="copy">© 2010 by Lars K. Brenner</div>
  <div class="fcol" style="left:191px"><b>SERVICE</b><br><span>Seminar<br>Events</span></div>
  <div class="fcol" style="left:268px"><b>NEWS</b><br><span>Seminar<br>Events</span></div>
  <div class="fcol" style="left:341px"><b>LINKS</b><br><span>Seminar<br>Events</span></div>
  <div class="fcol" style="left:406px"><b>GLOSSAR</b><br><span>Seminar<br>Events</span></div>
  <div class="flinks"><span>AGB</span><span>Impressum</span><span>Kontakt</span></div>
  <div class="note"><b>Wichtiger Hinweis:</b><br>Hiermit distanziere ich mich ausdrücklich von den Inhalten aller fremden Internetseiten, auf die ich per Link von meinem Angebot verweise und mache diese Inhalte mir nicht zu eigen. Diese Erklärung gilt für alle auf meinen Internetseiten angebrachten Links.</div>
</footer>
</body>
</html>
```